Wordpress theme customised please - for new ecommerce homewares website

Hi, we need a wordpress theme customised for a business that will sell tea towels (aka kitchen towels/dish cloths).
We do not have a website currently, but wish to launch using wordpress + woocommerce + "the shopfront" theme (c/- plumkestrel).
BACKGROUND RE THE BUSINESS
Our products are very stylish and will appeal to people who like owning gorgeous things - people who love cooking and/or decorating their home beautifully, or maybe they like travelling and/or buying presents for themselves and friends/family etc.
As they are typically used in people's kitchens, so "fresh" and "clean" is important - however the site must look very upmarket: timeless yet current, and classic yet simple, but not pretty, fussy or edgy.
We believe we have a great opportunity to leverage the "feel" of the product - cotton & linen fabric that has real texture to it, is tactile, natural, raw, real... in the photos used on the website, the backgrounds etc
Our logo is attached - a very dark grey colour was chosen, with white stripes, so that its neutral colouring would coordinate well with our suppliers' existing packaging. (We will represent a number of brands.)
BACKGROUND RE THIS PROJECT
We already know we want to use "the shopfront" theme by plumkestrel, but we need help customising the look of this theme so it works well with our logo, looks really striking and doesn't look like everyone else's ie "straight out of the box".
It appears these are the types of things that can be changed:
LAYOUT:
home page design concept (eg with a cascade carousel)
page design concept for eg About Us, Contact Us, FAQs
landing page design concept
header; light footer; dark footer
COLOURS & BACKGROUNDS & BORDERS & SEPARATORS:
main theme colour; accent colour; primary font colour
header background; light footer background colour; dark footer background colour; copyright bar background colour
dark footer widget title border; dark footer list separators and borders; dark footer/copyright bar separator styles
FONTS:
main navigation text colour; secondary navigation text colour; dark footer text colour; copyright bar text colour
main font; secondary font
LASTLY
Please don't hesitate to ask questions, request further information etc This is the first time we've posted a design project like this so it's tricky to know what other information you will need, so please just get in touch, ok!
Thanks so much for your interest in this project, and best wishes.

```html
<!DOCTYPE html>
<html lang="en">
<head>
<meta charset="utf-8">
<title>Dishcloth Guild</title>
<link href="https://fonts.googleapis.com/css2?family=Arvo:wght@400;700&family=Lato:wght@400;700;900&display=swap" rel="stylesheet">
<style>
:root{
  --ink:#252a36;
  --ink-soft:#3a3f4a;
  --header-bg:#f3f3f3;
  --page-bg:#ffffff;
  --muted:#8a8a8a;
  --rule:#d4d4d4;
  --badge:#7682a0;
  --white:#ffffff;
}
*{margin:0;padding:0;box-sizing:border-box}
html,body{width:1200px;height:1036px;overflow:hidden;background:var(--page-bg);font-family:'Lato',sans-serif;color:var(--ink)}
.page{position:relative;width:1200px;height:1036px}
.abs{position:absolute}

.topbar{left:0;top:0;width:1200px;height:26px;background:var(--ink);color:var(--white);font-size:11px;font-weight:700;letter-spacing:-.1px}
.topbar .promo{left:64px;top:6px}
.topbar .util{top:6px}
.topbar .search{left:904px;top:0;width:202px;height:26px;background:var(--white);border:1px solid var(--ink)}
.topbar .search-btn{left:1106px;top:0;width:40px;height:26px;background:var(--ink);display:flex;align-items:center;justify-content:center}

.header{left:0;top:26px;width:1200px;height:151px;background:var(--header-bg)}
.brand{left:65px;top:70px;height:50px;display:flex;align-items:center;font-family:'Arvo',serif;font-weight:700;font-size:34px;letter-spacing:1px;color:var(--ink);white-space:nowrap}
.main-nav{left:480px;top:72px;display:flex;gap:0;font-size:12.5px;font-weight:900;text-transform:uppercase}
.main-nav span{display:flex;align-items:center;margin-right:28px}
.main-nav span svg{margin-left:8px}
.nav-rule{left:480px;top:96px;width:482px;height:1px;background:var(--rule)}
.sub-nav{right:243px;top:104px;font-family:'Arvo',serif;font-size:13px;color:var(--muted);white-space:nowrap}
.sub-nav i{font-style:normal;margin:0 10px;color:#b5b5b5}
.bag{left:997px;top:61px;width:150px;height:69px;border:1px solid var(--rule);background:var(--white)}
.bag .label{left:11px;top:12px;font-size:12px;font-weight:900;display:flex;align-items:center;gap:18px}
.bag .rule{left:11px;top:33px;width:127px;height:1px;background:var(--rule)}
.bag .total{left:11px;top:43px;font-family:'Arvo',serif;font-size:13px;color:var(--muted);white-space:nowrap}
.bag .total i{font-style:normal;margin:0 8px;color:#b5b5b5}

.tile{top:203px;width:345px;height:518px;overflow:hidden;color:var(--white);text-align:center}
.tile .photo{position:absolute;inset:0}
.tile .veil{position:absolute;left:12px;top:12px;right:12px;bottom:12px;background:rgba(140,145,155,.45)}
.tile .title{position:absolute;left:0;right:0;top:218px;font-family:'Arvo',serif;font-weight:700;font-size:25px;text-shadow:0 1px 3px rgba(0,0,0,.35)}
.tile .bar{position:absolute;left:138px;top:261px;width:69px;height:2px;background:var(--white)}
.tile .caption{position:absolute;left:0;right:0;top:276px;font-family:'Arvo',serif;font-size:15px;text-shadow:0 1px 3px rgba(0,0,0,.35)}

.shipping{left:65px;top:755px;width:1082px;height:138px;background:var(--ink);color:var(--white)}
.shipping .frame{left:12px;top:12px;width:1058px;height:114px;border:2px solid var(--white)}
.shipping .headline{left:0;width:940px;top:30px;text-align:center;font-weight:700;font-size:24px;letter-spacing:-.2px}
.shipping .headline b{font-size:36px;font-weight:900;vertical-align:-2px}
.shipping .underline{left:276px;top:72px;width:530px;height:2px;background:var(--white)}
.shipping .note{left:0;width:940px;top:81px;text-align:center;font-size:16px}
.badge{left:944px;top:741px;width:162px;height:162px;border-radius:50%;background:var(--badge);color:var(--white);text-align:center;font-size:17px;line-height:19px;padding-top:40px}
.badge b{display:block;font-size:22px;font-weight:900;line-height:26px}

.divider{left:65px;top:937px;width:1082px;height:1px;background:var(--rule)}
.section-title{left:67px;top:968px;font-family:'Arvo',serif;font-weight:700;font-size:15px;letter-spacing:.3px}
.section-bar{left:65px;top:1018px;width:69px;height:2px;background:var(--ink)}
.arrows{left:1058px;top:958px}
</style>
</head>
<body>
<div class="page">

  <div class="abs topbar">
    <span class="abs promo">FREE SHIPPING ON ALL ORDERS OVER $80.00 OR MORE!</span>
    <span class="abs util" style="left:668px">TRACK YOUR ORDER</span>
    <span class="abs util" style="left:804px">MY ACCOUNT</span>
    <div class="abs search"></div>
    <div class="abs search-btn">
      <svg width="13" height="13" viewBox="0 0 13 13"><circle cx="5.3" cy="5.3" r="3.9" fill="none" stroke="#fff" stroke-width="2"/><line x1="8.2" y1="8.2" x2="12" y2="12" stroke="#fff" stroke-width="2.2" stroke-linecap="round"/></svg>
    </div>
  </div>

  <header class="abs header" style="top:26px"></header>

  <div class="abs brand">DISHCLOTH GUILD</div>

  <nav class="abs main-nav">
    <span>Home<svg width="7" height="5" viewBox="0 0 7 5"><path d="M1 1l2.5 2.5L6 1" fill="none" stroke="#252a36" stroke-width="1.2"/></svg></span>
    <span>Shop By<svg width="7" height="5" viewBox="0 0 7 5"><path d="M1 1l2.5 2.5L6 1" fill="none" stroke="#252a36" stroke-width="1.2"/></svg></span>
    <span>All Pages<svg width="7" height="5" viewBox="0 0 7 5"><path d="M1 1l2.5 2.5L6 1" fill="none" stroke="#252a36" stroke-width="1.2"/></svg></span>
    <span>Shortcodes<svg width="7" height="5" viewBox="0 0 7 5"><path d="M1 1l2.5 2.5L6 1" fill="none" stroke="#252a36" stroke-width="1.2"/></svg></span>
    <span>Blog<svg width="7" height="5" viewBox="0 0 7 5"><path d="M1 1l2.5 2.5L6 1" fill="none" stroke="#252a36" stroke-width="1.2"/></svg></span>
  </nav>
  <div class="abs nav-rule"></div>
  <div class="abs sub-nav">All Products<i>|</i>Lookbook<i>|</i>Sales<i>|</i>Gift Cards</div>

  <div class="abs bag">
    <div class="abs label">SHOPPING BAG<svg width="7" height="5" viewBox="0 0 7 5"><path d="M1 1l2.5 2.5L6 1" fill="none" stroke="#252a36" stroke-width="1.2"/></svg></div>
    <div class="abs rule"></div>
    <div class="abs total">€66.94<i>/</i>2 Items</div>
  </div>

  <a class="abs tile" style="left:65px">
    <div class="photo" role="img" aria-label="Natural linen tea towels with black stripes, dots and bold shapes hanging from white hooks" style="background:linear-gradient(160deg,#e4e0d8 0%,#cfc9bf 45%,#a9a39a 100%)"></div>
    <div class="title">SHOP SALE</div>
    <div class="bar"></div>
    <div class="caption">The sale don't stop up to 75% off!</div>
  </a>

  <a class="abs tile" style="left:433px">
    <div class="photo" role="img" aria-label="Grey-striped and orange-striped tea towels hanging from white hooks" style="background:linear-gradient(135deg,#d9d9d9 0%,#a6a39f 40%,#c98a5a 75%,#e07a3a 100%)"></div>
    <div class="veil"></div>
    <div class="title">ACCESSORIES</div>
    <div class="bar"></div>
    <div class="caption">The sale don't stop up to 75% off!</div>
  </a>

  <a class="abs tile" style="left:801px">
    <div class="photo" role="img" aria-label="White tea towels with grey, mint, lime, orange and magenta lettered stripes hanging in a row" style="background:linear-gradient(100deg,#e6e6e3 0%,#cfe0da 30%,#d5dca6 50%,#f0b48a 72%,#d98cc0 100%)"></div>
    <div class="title">LOOKBOOK</div>
    <div class="bar"></div>
    <div class="caption">Take a look at the upcoming trends.</div>
  </a>

  <section class="abs shipping">
    <div class="abs frame"></div>
    <div class="abs headline">FREE SHIPPING ON ALL ORDERS OVER <b>$75</b></div>
    <div class="abs underline"></div>
    <div class="abs note">*FREE OVER $125 FOR INTERNATIONAL ORDERS</div>
  </section>
  <div class="abs badge">DELIVERED<br>TO YOUR<br>DOOR<b>IN 4 DAYS</b></div>

  <div class="abs divider"></div>
  <h2 class="abs section-title">FEATURED PRODUCTS</h2>
  <div class="abs section-bar"></div>
  <svg class="abs arrows" width="90" height="42" viewBox="0 0 90 42">
    <circle cx="20" cy="21" r="19" fill="none" stroke="#555" stroke-width="1.5"/>
    <path d="M23 13l-8 8 8 8" fill="none" stroke="#555" stroke-width="1.5"/>
    <circle cx="68" cy="21" r="19" fill="none" stroke="#555" stroke-width="1.5"/>
    <path d="M65 13l8 8-8 8" fill="none" stroke="#555" stroke-width="1.5"/>
  </svg>

</div>
</body>
</html>
```